Business card designed for promo code

Design a basic business card that we can fill in promo code

This business card will be designed to be left with gyms and trainers so that they can have personal promo codes to get there clients discounts.

Font Content :
Logo with Slogan (slogan can be all put on one line if it will fit better)
Text list of services " DXA Body Composition - VO2 Cardio Fitness Test - Metabolic Health Test "
Basic contact info - phone, email, web address, physical address

Back Content:
Brivolen Affiliates Discount
Take _15%_ off single services and select packages*
Promo Code __________________
Book appointments online at www. BRIVOLEN.com
*Excludes Gold Tier

Target Market(s)

Fitness Industry

Industry/Entity Type

Fitness

Contact Information for Business Card

Modern / simple card -- leave large enough blank line so we can write in promo codes

Requirements
Must have
• Similar color and feel to current card design
• Best if back of card has white background so that we can write in promo code and it will be readable
Nice to have
• Line on back for expiration date if you can make it look good and it fits
Should not have
• Does not need to have name or position on card
• We have all have our individual cards .. i want this to be generic info for business only

```html
<!DOCTYPE html>
<html lang="en">
<head>
<meta charset="utf-8">
<title>Brivolen Affiliates Discount Card</title>
<link rel="stylesheet" href="https://fonts.googleapis.com/css2?family=Questrial&display=swap">
<style>
  :root {
    --card-white: #ffffff;
    --brand-blue: #42c6fb;
    --accent-blue: #2f86f0;
    --brand-slate: #758a8f;
    --ink: #111111;
    --field-white: #ffffff;
  }
  html, body {
    margin: 0;
    padding: 0;
    width: 1200px;
    height: 622px;
    overflow: hidden;
    background: var(--card-white);
  }
  .card {
    position: relative;
    width: 1200px;
    height: 622px;
    overflow: hidden;
    background: var(--card-white);
    font-family: "Questrial", "Century Gothic", sans-serif;
    color: var(--ink);
  }
  .card__wave {
    position: absolute;
    left: 0;
    top: 0;
    width: 1200px;
    height: 622px;
  }
  .offer {
    position: absolute;
    left: 88px;
    top: 206px;
  }
  .offer__title {
    margin: 0;
    font-weight: 400;
    font-size: 67px;
    line-height: 1;
    letter-spacing: 0.2px;
    white-space: nowrap;
  }
  .offer__title-accent {
    color: var(--accent-blue);
  }
  .offer__terms {
    margin: 5px 0 0 1px;
    font-size: 21.8px;
    line-height: 1.2;
    letter-spacing: 0.3px;
    white-space: nowrap;
  }
  .address {
    position: absolute;
    left: 89px;
    top: 359px;
    margin: 0;
    font-style: normal;
    font-size: 21px;
    line-height: 27px;
  }
  .brand-name {
    position: absolute;
    left: 760px;
    top: 200px;
    width: 380px;
    text-align: center;
    font-size: 66px;
    line-height: 1;
    color: var(--brand-slate);
  }
  .promo__label {
    position: absolute;
    left: 127px;
    top: 531px;
    font-size: 41px;
    line-height: 42px;
    color: var(--card-white);
    letter-spacing: 0.6px;
    word-spacing: 8px;
    white-space: nowrap;
  }
  .promo__field {
    position: absolute;
    left: 514px;
    top: 532px;
    width: 567px;
    height: 41px;
    border-radius: 20px;
    background: var(--field-white);
  }
</style>
</head>
<body>
  <main class="card">
    <svg class="card__wave" viewBox="0 0 1200 622" aria-hidden="true">
      <path d="M0 438 C 120 458, 240 466, 360 463 C 500 459, 620 440, 740 435 L 1200 436 L 1200 622 L 0 622 Z" fill="var(--brand-blue)"/>
    </svg>

    <section class="offer">
      <h1 class="offer__title">Affiliates <span class="offer__title-accent">Discount</span></h1>
      <p class="offer__terms">Take 15% of Singles Servises and Selected Packages</p>
    </section>

    <address class="address">418 Larkmoor Avenue<br>Fernbridge, IL 60218</address>

    <div class="brand-name">Brivolen</div>

    <span class="promo__label">Promotional Code:</span>
    <span class="promo__field"></span>
  </main>
</body>
</html>
```